Tidewell Electrical Solutions

On one side. LOGO (underneath:) Commercial Industrial Residential

- NAME & CONTACT DETAILS

Martin K. Oduya
Project Manager

(Cell icon) (441) 555-0187
(Email icon) twlelectricalsoultions@mailpost-demo.com
(Facebook & Instagram icons )@twlelectricalsolutions

Other side: LOGO - underneath ELECTRICAL CONSTRUCTION & MAINTENANCE . LED LIGHTING & AUTOMATION . LIFE SAFETY SYSTEMS (FIRE ALARM / SECURITY) . DATA & COMMUNICATION

```html
<!DOCTYPE html>
<html lang="en">
<head>
<meta charset="utf-8">
<title>Tidewell Electrical Solutions – Business Card</title>
<link href="https://fonts.googleapis.com/css2?family=Open+Sans:wght@400;600;700&display=swap" rel="stylesheet">
<style>
  :root {
    --backdrop: #262626;
    --teal: #195a6d;
    --white: #ffffff;
    --paper: #fbfbfb;
    --ink: #3a3a3a;
    --rule: #6b6b6b;
  }
  * { box-sizing: border-box; margin: 0; padding: 0; }
  html, body { width: 1200px; height: 1021px; overflow: hidden; }
  body {
    background: var(--backdrop);
    font-family: "Open Sans", Arial, sans-serif;
    position: relative;
  }
  .card {
    position: absolute;
    left: 260px;
    width: 680px;
    height: 388px;
    box-shadow: 0 10px 28px rgba(0,0,0,.5);
  }
  /* Back side */
  .card--back { top: 90px; background: var(--teal); color: var(--white); }
  .card--back .wordmark {
    position: absolute; left: 0; right: 0; top: 120px;
    text-align: center;
    font-size: 40px; font-weight: 600; letter-spacing: 1px;
  }
  .card--back .services {
    position: absolute; left: 40px; right: 40px; top: 250px;
    text-align: center;
    font-size: 17px; line-height: 1.5;
  }
  /* Front side */
  .card--front { top: 518px; background: linear-gradient(180deg, var(--paper), #ececec); color: var(--ink); }
  .person { position: absolute; left: 48px; top: 48px; }
  .person__name {
    color: var(--teal); font-weight: 700; font-size: 22px; text-transform: uppercase;
  }
  .person__title { font-size: 16px; margin-top: 2px; }
  .brand { position: absolute; right: 48px; top: 44px; text-align: right; }
  .brand__name { color: var(--teal); font-size: 22px; font-weight: 600; }
  .brand__sectors { font-size: 16px; margin-top: 8px; }
  .divider {
    position: absolute; left: 48px; right: 48px; top: 158px;
    border-top: 1px solid var(--rule);
  }
  .contacts {
    position: absolute; right: 48px; bottom: 40px;
    list-style: none; text-align: right; font-size: 17px; line-height: 1.7;
  }
  .contacts li { display: flex; align-items: center; justify-content: flex-end; gap: 10px; }
  .contacts svg { width: 16px; height: 16px; flex: none; }
</style>
</head>
<body>
  <section class="card card--back" aria-label="Card back">
    <div class="wordmark">Tidewell Electrical Solutions</div>
    <p class="services">
      Electrical Construction &amp; Maintenance • Led Lighting &amp; Automation<br>
      Life Safety Systems (Fire Alarm / Security) • Data &amp; Communication
    </p>
  </section>

  <section class="card card--front" aria-label="Card front">
    <div class="person">
      <div class="person__name">Martin K. Oduya</div>
      <div class="person__title">Project Manager</div>
    </div>
    <div class="brand">
      <div class="brand__name">Tidewell Electrical Solutions</div>
      <div class="brand__sectors">Commercial Industrial Residential</div>
    </div>
    <div class="divider"></div>
    <ul class="contacts">
      <li>(441) 555-0187
        <svg viewBox="0 0 16 16" aria-hidden="true"><rect x="4" y="1" width="8" height="14" rx="1.5" fill="none" stroke="#195a6d" stroke-width="1.5"/><line x1="7" y1="12.5" x2="9" y2="12.5" stroke="#195a6d" stroke-width="1.2"/></svg></li>
      <li>twlelectricalsoultions@mailpost-demo.com
        <svg viewBox="0 0 16 16" aria-hidden="true"><rect x="1" y="3" width="14" height="10" fill="none" stroke="#195a6d" stroke-width="1.5"/><polyline points="1,3 8,9 15,3" fill="none" stroke="#195a6d" stroke-width="1.5"/></svg></li>
      <li>@twlelectricalsolutions
        <svg viewBox="0 0 16 16" aria-hidden="true"><rect x="1.5" y="1.5" width="13" height="13" rx="3" fill="none" stroke="#195a6d" stroke-width="1.5"/></svg></li>
      <li>@twlelectricalsolutions
        <svg viewBox="0 0 16 16" aria-hidden="true"><rect x="1.5" y="1.5" width="13" height="13" rx="2" fill="#195a6d"/></svg></li>
    </ul>
  </section>
</body>
</html>
```